Sifu Tomaso's First Book - research in Wing Chun Kung Fu

Sifu Tomaso (www.sifutomaso.example) is the founder and Worldwide Head Instructor of his Wing Chun Kung Fu organization, the GRBF. To get his extensive research out to the world, he has written his first book which counts well over 400 pages and needs to hit the shelves as soon as possible.

We are looking for a graphic designer (a cover at first, but if you think you can design the whole INSIDE of the book, we are more than happy to look at your designs!) who understands the targetgroup to which this book has to appeal: kung fu lovers, GRBF students and martial arts affiliates. The highly anticipated book counts around 400 pages and features 50/50 text and photos. It promises to have a grand impact on the martial arts community.

Front Cover Info:
Title of the book: The Nine Quiet Pillars
Undertitle: The BDR and history of Crane Palm
Writer: Sifu Tomaso Iadarola

Coloursuggestion to possibly work with: yellow and black
Think oriental/Chinese but wrapped in modern Western design. Please feel free to go crazy, though professional.
Backgroundinfo can be found on http://www.palmrivera.example/grbf/sifu-tomaso-grbf-palm-river-system/ and http://sifutomaso.example/biography/. Many additional info can be found on these websites.

Extra info:
- estimated publishing: 40.000 pax.

Attachments:
- the GRBF logo has to be on the front of the book somewhere
- the Sifu Tomaso logo (SIFU TOMASO wordmark) has to be on the spine of the book

Industry/Entity Type

Graphic Designer

Requirements
Must have
• - Front cover must have image of author (see attachment) WITHOUT the Sifu Tomaso logo: the author has to look up to the book title.
• - the double S symbol of the Sifu Tomaso logo (see attachment) to be placed at the bottom of the spine of the book along with the author's name and booktitle. Note: SIFU TOMASO wordmark has to be readible when the book it is vertical.

```html
<!DOCTYPE html>
<html lang="en">
<head>
<meta charset="utf-8">
<title>The Nine Quiet Pillars — Book Cover</title>
<link rel="stylesheet" href="https://fonts.googleapis.com/css2?family=Anton&family=Arimo&display=swap">
<style>
  :root {
    --sky-top: #d98f0f;
    --sky-mid: #f6c22c;
    --sky-glow: #fde98a;
    --ink: #000000;
    --paper: #ffffff;
    --cream: #f1ecd6;
    --accent: #f29a1f;
    --photo-grey: #8a8a8a;
  }
  * { margin: 0; padding: 0; box-sizing: border-box; }
  html, body { width: 1200px; height: 848px; overflow: hidden; background: var(--ink); }
  .cover {
    position: relative;
    width: 1200px;
    height: 848px;
    overflow: hidden;
    font-family: "Anton", "Arial Narrow", sans-serif;
    color: var(--ink);
  }
  .sky {
    position: absolute;
    inset: 0;
    background:
      radial-gradient(ellipse 380px 260px at 860px 230px, var(--sky-glow) 0%, rgba(253,233,138,0) 70%),
      linear-gradient(180deg, var(--sky-top) 0%, var(--sky-mid) 35%, #f4b51f 60%, #d8900c 80%);
  }
  .hills { position: absolute; inset: 0; }
  .title { position: absolute; text-align: center; text-transform: uppercase; line-height: 0.95; }
  .title__top, .title__main, .title__sub { display: block; }
  .back-title { left: 120px; top: 68px; width: 300px; }
  .back-title .title__top { font-size: 50px; }
  .back-title .title__main { font-size: 74px; margin-top: -2px; }
  .back-title .title__sub { font-size: 17px; margin-top: 2px; letter-spacing: 0.2px; }
  .front-title { left: 705px; top: 36px; width: 430px; }
  .front-title .title__top { font-size: 88px; }
  .front-title .title__main { font-size: 128px; margin-top: -4px; }
  .front-title .title__sub { font-size: 26px; margin-top: 2px; }
  .blurb {
    position: absolute;
    left: 82px; top: 450px; width: 390px;
    font-family: "Arimo", Arial, sans-serif;
    font-size: 13.5px; line-height: 21.5px;
    color: var(--paper); text-align: center;
  }
  .spine {
    position: absolute; left: 565px; top: 0; width: 70px; height: 848px;
  }
  .spine__title {
    position: absolute; left: 14px; top: 40px;
    writing-mode: vertical-rl;
    font-size: 38px; letter-spacing: 1px; text-transform: uppercase;
    color: var(--ink);
  }
  .spine__mark {
    position: absolute; left: 22px; top: 408px;
    writing-mode: vertical-rl;
    display: flex; align-items: center; gap: 6px;
    font-size: 16px; color: var(--accent); text-transform: uppercase;
  }
  .spine__mark-dot { width: 10px; height: 10px; border-radius: 50%; background: var(--accent); }
  .spine__author {
    position: absolute; left: 22px; top: 600px;
    writing-mode: vertical-rl;
    font-size: 20px; letter-spacing: 0.5px; color: var(--paper); text-transform: uppercase;
  }
  .author-name {
    position: absolute; left: 668px; top: 776px;
    font-size: 33px; letter-spacing: 1px; color: var(--cream); text-transform: uppercase;
  }
  .author-photo {
    position: absolute; left: 1010px; top: 600px; width: 178px; height: 248px;
    background: linear-gradient(180deg, #5a5a5a 0%, var(--photo-grey) 45%, #6e6e6e 100%);
  }
</style>
</head>
<body>
<main class="cover">
  <div class="sky" role="img" aria-label="Golden sunset sky with silhouettes of kung fu practitioners on a hilltop"></div>
  <svg class="hills" width="1200" height="848" viewBox="0 0 1200 848" aria-hidden="true">
    <path d="M0 402 C80 392 160 372 250 366 C330 362 420 410 500 455 C560 490 620 540 700 578 C760 590 900 586 1200 578 L1200 848 L0 848 Z" fill="var(--ink)"/>
  </svg>

  <h2 class="title back-title">
    <span class="title__top">The Nine Quiet</span>
    <span class="title__main">Pillars</span>
    <span class="title__sub">The BDR and history of Crane Palm</span>
  </h2>

  <p class="blurb">Lorem ipsum dolor sit amet, felis nulla vulputate est vestibulum egestas dui. Porta tincidunt sed commodo magnis, luctus malesuada dignissim eget, id condimentum convallis in orci a pretium, orci eget vel. Lacinia dui quis dui sodales, vel aenean morbi. Excepturi inceptos, elit ut molestie, luctus lectus eget velit nunc, mauris in dolor eget. Ligula sed molestie lectus scelerisque odio non, adipiscing et ut turpis commodo auctor convallis.</p>

  <section class="spine">
    <span class="spine__title">The Nine Quiet Pillars</span>
    <span class="spine__mark"><span class="spine__mark-dot"></span>Sifu Tomaso</span>
    <span class="spine__author">Sifu Tomaso Venturelli</span>
  </section>

  <h1 class="title front-title">
    <span class="title__top">The Nine Quiet</span>
    <span class="title__main">Pillars</span>
    <span class="title__sub">The BDR and history of Crane Palm</span>
  </h1>

  <div class="author-photo" role="img" aria-label="Black and white photo of the author looking up toward the title, arms crossed"></div>
  <p class="author-name">Sifu Tomaso Venturelli</p>
</main>
</body>
</html>
```